R & K Fabworks Brochure

We need a 2 page (front and back) full color brochure for our Mechanical Contracting company. The website is http://www.rkfabworks.example although we're looking for something fresh. If anything the future web design might follow the design of this brochure more than we'd like to have the brochure follow the design of the website. However, to start please use content found on the website and we will refine. We want basically a cover, 2 inner pages and a back. Attached is a an example brochure from another company as well as an outdated brochure we used previously.

Target Market(s)

1. Industrial, Commercial and Institutional Builders and Owners

2. Industrial, Commercial and Institutional HVAC Service customers

Industry/Entity Type

It Company

Font styles to use
Serif
Sans Serif

Requirements
Must have
• Strong imagery
Should not have
• Plumbing Service
Pictures of people besides Owner Marlon Quigsby and President Dustin Okafor

```html
<!DOCTYPE html>
<html lang="en">
<head>
<meta charset="utf-8">
<title>R &amp; K Fabworks Brochure</title>
<link rel="stylesheet" href="https://fonts.googleapis.com/css2?family=Source+Sans+3:wght@400;600&display=swap">
<style>
  :root{
    --stage:#4a4a4a;
    --paper:#ffffff;
    --navy:#1c3a8c;
    --royal:#2a58be;
    --sky:#7db4ea;
    --sun:#f2cb3d;
    --ink:#3a3a3a;
    --ink-soft:#555;
    --photo-dark:#2a2f3a;
    --photo-light:#9fb6cf;
  }
  *{box-sizing:border-box;margin:0;padding:0}
  html,body{width:1200px;height:720px;overflow:hidden}
  body{background:var(--stage);font-family:"Source Sans 3",Arial,sans-serif;color:var(--ink);position:relative}
  .page{position:absolute;top:10px;width:540px;height:700px;background:var(--paper);overflow:hidden}
  .page--front{left:40px}
  .page--back{left:620px}
  .page svg.swoosh{position:absolute;inset:0;width:540px;height:700px}

  /* front */
  .cover-band{position:absolute;left:0;top:0;width:540px;height:170px;background:linear-gradient(135deg,var(--navy),var(--royal) 60%,#3b74d2)}
  .cover-headline{position:absolute;left:38px;top:62px;width:330px;color:#fff;font-size:22px;line-height:1.2;font-weight:400}
  .accent-bar{position:absolute;height:9px}
  .cover-photo{position:absolute;left:0;top:179px;width:540px;height:300px;background:linear-gradient(160deg,var(--photo-dark) 0%,#4c5a70 45%,var(--photo-light) 70%,#3a3f48 100%)}
  .cover-tagline{position:absolute;left:40px;top:520px;width:330px;font-size:23px;line-height:1.2;color:var(--ink-soft)}
  .brand{position:absolute;display:flex;align-items:center;gap:8px;font-weight:600;color:var(--navy)}
  .brand-square{width:22px;height:22px;background:var(--navy)}
  .cover-brand{right:36px;top:528px;font-size:17px}
  .cover-web{position:absolute;left:40px;bottom:36px;font-size:13px;color:var(--ink-soft)}

  /* back */
  .bio{position:absolute;left:30px;width:320px;font-size:8.5px;line-height:1.35;color:var(--ink)}
  .bio-title{font-weight:600;font-size:9.5px;margin-bottom:3px}
  .bio--first{top:110px}
  .bio--second{top:200px}
  .headshot{position:absolute;left:372px;width:104px;height:78px;background:linear-gradient(160deg,#cfd6de,#6a7482)}
  .headshot--first{top:92px}
  .headshot--second{top:184px}
  .back-brand{left:34px;top:338px;font-size:14px}
  .contact{position:absolute;left:150px;top:334px;font-size:9px;line-height:1.35;font-style:normal}
  .contact strong{font-weight:600}
  .directions{position:absolute;width:220px;font-size:9px;line-height:1.35}
  .directions h3{font-size:9.5px;font-weight:600}
  .directions--west{left:36px;top:520px}
  .directions--east{left:300px;top:470px}
</style>
</head>
<body>

<section class="page page--front">
  <div class="cover-band"></div>
  <h1 class="cover-headline">R &amp; K designs, builds, installs and services Heating, Ventilation and Air Conditioning.</h1>
  <div class="accent-bar" style="left:0;top:170px;width:180px;background:var(--royal)"></div>
  <div class="accent-bar" style="left:184px;top:170px;width:170px;background:var(--sun)"></div>
  <div class="accent-bar" style="left:358px;top:170px;width:182px;background:var(--sun)"></div>
  <div class="cover-photo" role="img" aria-label="Crew silhouettes lifting a panel into a large warehouse window at dusk"></div>
  <svg class="swoosh" viewBox="0 0 540 700" aria-hidden="true">
    <path d="M0 478 C180 476 390 420 540 300 L540 700 L0 700Z" fill="var(--paper)"/>
    <path d="M0 470 C180 468 390 412 540 292" fill="none" stroke="var(--royal)" stroke-width="10"/>
    <path d="M0 458 C180 456 390 398 540 276" fill="none" stroke="var(--sky)" stroke-width="5"/>
  </svg>
  <p class="cover-tagline">HVAC systems for commercial, industrial and residential applications.</p>
  <div class="brand cover-brand"><span class="brand-square"></span>R &amp; K Fabworks</div>
  <p class="cover-web">www.rkfabworks.example</p>
</section>

<section class="page page--back">
  <svg class="swoosh" viewBox="0 0 540 700" aria-hidden="true">
    <path d="M120 0 L540 0 L540 240 C500 100 360 18 120 0Z" fill="var(--royal)"/>
    <path d="M200 0 C390 20 500 90 540 200" fill="none" stroke="var(--sky)" stroke-width="6"/>
    <path d="M260 0 C420 22 510 80 540 150" fill="none" stroke="#fff" stroke-width="4"/>
    <rect x="0" y="300" width="150" height="10" fill="var(--royal)"/>
    <rect x="155" y="300" width="180" height="10" fill="var(--sun)"/>
    <rect x="340" y="300" width="200" height="10" fill="var(--sun)"/>
    <path d="M120 410 C300 412 460 380 540 330 L540 362 C450 410 300 432 120 424Z" fill="var(--royal)"/>
    <path d="M100 432 C300 436 470 400 540 370" fill="none" stroke="var(--sky)" stroke-width="5"/>
  </svg>

  <div class="bio bio--first">
    <p class="bio-title">Marlon Quigsby – CEO / Project Manager</p>
    <p>As owner and CEO, Marlon oversees all operations at R &amp; K Fabworks. With 14 years in mechanical contracting and a journeyman license, he drives quality control and safety on every job. He also manages major design-build projects and stays committed to the industry.</p>
  </div>
  <div class="headshot headshot--first" role="img" aria-label="Portrait of Marlon Quigsby"></div>

  <div class="bio bio--second">
    <p class="bio-title">Dustin Okafor – CEO / Project Manager</p>
    <p>As president, Dustin leads estimating and field crews at R &amp; K Fabworks. A licensed pipefitter with years on commercial sites, he keeps schedules tight and clients informed. Dustin also manages institutional projects and mentors new technicians entering the trade.</p>
  </div>
  <div class="headshot headshot--second" role="img" aria-label="Portrait of Dustin Okafor"></div>

  <div class="brand back-brand"><span class="brand-square"></span>R &amp; K</div>
  <address class="contact">
    <strong>R &amp; K Fabworks, Inc.</strong><br>
    418 Quarry Lane Ashby, OH 43999<br>
    Phone: 555-014-2290 &nbsp;Fax: 555-014-2291
  </address>

  <div class="directions directions--west">
    <h3>Driving Directions</h3>
    <p>Driving East or West on Route 7<br>Take Exit 21 to Highway 30<br>Take Exit 48 left on Mill Road<br>Turn left on Harbor Crossing<br>Turn left on Quarry Lane<br>R &amp; K is on the left</p>
  </div>
  <div class="directions directions--east">
    <h3>Driving East on Highway 30</h3>
    <p>Take Exit 48 to Mill Road<br>Turn left on Harbor Crossing<br>Turn left on Quarry Lane<br>R &amp; K is on the left</p>
  </div>
</section>

</body>
</html>
```